kx7-notiz.de
Zielgruppe
Alle die kein Geld haben :-)
Aufgabenstellung
Unter kx7-notiz.de sollen Informationen rund um Kredite, Kreditkarten, Belvra usw. entstehen. Diese werden dann unter Subdomains wir konto.kx7-notiz.de oder kreditkarte.kx7-notiz.de laufen. Die Domain kx7-notiz.de soll die Hauptdomain werden wofür ein Logo und ein Layout benötigt wird. Auf den einzelnen Seiten sollen später Reporte verkauft werden und relativ viel mit Zentrix Werbung gearbeitet werden. Hier ein paar Beipspiele www.morvel-hafen.biz, www.talvopunkt24.de, www.linden-blau-bote.de, www.gerlinde-wolken-bote.de
Die genannten Seiten sind keine Meisterleistung in Design und sollen nur in etwa Inhalte und die Einbindung von Zentrix Adfolio wieder geben. Menüpunkte sind immer gleich und werden sein mit den Untertiteln wie bei www.morvel-hafen.biz.

```html
<!DOCTYPE html>
<html lang="de">
<head>
<meta charset="utf-8">
<title>kx7-notiz.de</title>
<link href="https://fonts.googleapis.com/css2?family=Arimo:wght@400;700&display=swap" rel="stylesheet">
<style>
:root{
  --orange:#f27b12;
  --orange-light:#ff9f3a;
  --dark:#2c2c2c;
  --darker:#222;
  --mid:#3a3a3a;
  --grey:#8a8a8a;
  --line:#d6d6d6;
  --text:#333;
  --soft:#f2f2f2;
}
*{box-sizing:border-box;margin:0;padding:0}
html,body{width:1200px;height:1198px;overflow:hidden;background:#fff;font-family:"Arimo",Arial,sans-serif;color:var(--text)}
.page{position:relative;width:1200px;height:1198px}
.site-header{position:absolute;left:0;top:0;width:1200px;height:108px}
.brand{position:absolute;left:163px;top:28px;font-size:42px;font-weight:700;color:var(--text);letter-spacing:-1px}
.topbar{position:absolute;left:0;top:108px;width:1200px;height:41px;background:linear-gradient(#3c3c3c,#242424);color:#fff;font-size:11.5px;line-height:41px;padding-left:163px}
.band{position:absolute;left:0;top:149px;width:1200px;height:283px;background:linear-gradient(90deg,var(--orange),var(--orange-light) 50%,var(--orange))}
.main-nav{position:absolute;left:120px;top:149px;width:276px;height:283px;background:var(--dark);padding:10px 14px}
.main-nav .item{margin-bottom:12px;font-size:11.5px;line-height:13px;color:#ddd}
.main-nav .item b{display:block;color:#fff;font-size:13.5px;line-height:16px}
.main-nav .item span{display:block;color:var(--orange)}
.hero{position:absolute;left:396px;top:149px;width:684px;height:283px;background:#fff}
.hero-visual{position:absolute;left:0;top:0;width:684px;height:262px;background:radial-gradient(ellipse at 50% 55%,#e9e9e9,#fafafa 70%)}
.hero-caption{position:absolute;left:0;top:262px;width:684px;text-align:center;font-size:12.5px;font-weight:700;color:#555;letter-spacing:.3px}
.side-list{position:absolute;left:120px;top:440px;width:276px;height:472px;background:var(--dark);padding:10px 12px}
.side-list .entry{margin-bottom:13px;font-size:11.5px;line-height:13.5px;color:#ddd}
.side-list .entry b{display:block;color:#fff;font-size:13.5px;line-height:17px}
.side-list .entry span{display:block;color:var(--orange)}
.content{position:absolute;left:410px;top:440px;width:394px;font-size:11.5px;line-height:13.5px}
.content h1{font-size:17px;font-weight:400;color:var(--orange);margin-bottom:8px}
.content p{margin-bottom:13px}
.offers{position:absolute;left:816px;top:440px;width:264px;height:470px;border:1px solid var(--line);background:#fff}
.offers h2{background:var(--soft);border-bottom:1px solid var(--line);font-size:12.5px;color:#666;padding:7px 10px;letter-spacing:.5px}
.offers .entry{padding:0 10px;margin-top:12px;font-size:11.5px;line-height:13.5px}
.offers .entry b{display:block;font-size:13px;line-height:16px;color:var(--text)}
.offers .entry span{display:block;color:var(--orange)}
.site-footer{position:absolute;left:120px;top:972px;width:960px;height:170px;background:var(--mid);display:flex;padding:20px 16px}
.site-footer .col{flex:1;padding-right:16px}
.site-footer h3{font-size:12.5px;color:#fff;border-bottom:1px solid #666;padding-bottom:5px;margin-bottom:6px}
.site-footer li{list-style:none;font-size:11px;line-height:15.5px;color:#999;padding-left:12px;position:relative}
.site-footer li::before{content:"";position:absolute;left:2px;top:6px;width:4px;height:4px;background:var(--orange)}
.legal{position:absolute;left:120px;top:1152px;width:960px;font-size:11px;color:var(--grey)}
.legal .links{position:absolute;right:0;top:0;color:var(--orange)}
</style>
</head>
<body>
<div class="page">
  <header class="site-header"><div class="brand">kx7-notiz.de</div></header>
  <div class="topbar">Lorem ipsum dolor sit amet, consetetur sadipscing elitr, sed diam nonumy eirmod tempor invidunt ut labore et dolore magna aliquyam erat, sed diam voluptua.</div>
  <div class="band"></div>
  <nav class="main-nav">
    <div class="item"><b>Startseite</b>Infos zu unserem Report<span>kx7-notiz.de</span></div>
    <div class="item"><b>Bestellen</b>Bestellen Sie unseren Report<span>kx7-notiz.de/bestellung.htm</span></div>
    <div class="item"><b>Kontakt</b>Treten Sie mit uns in Kontakt<span>kx7-notiz.de/kontakt.htm</span></div>
    <div class="item"><b>Datenschutz</b>Hinweise zum Datenschutz<span>kx7-notiz.de/datenschutz.htm</span></div>
    <div class="item"><b>Impressum</b>Unsere Anschrift für Fragen<span>kx7-notiz.de/impressum.htm</span></div>
  </nav>
  <section class="hero">
    <div class="hero-visual" role="img" aria-label="Illustration: Figuren stehen um einen orangefarbenen Datenbank-Zylinder"></div>
    <div class="hero-caption">Unsere Datenbank umfasst Informationen zu Kredite, Kreditkarten, Belvra u.v.m.</div>
  </section>
  <aside class="side-list">
    <div class="entry"><b>ALG II / Hartz IV Kredite</b>Kredithelfer für ALG und Hartz IV Empfänger<span>www.talvo-stufe-info.de</span></div>
    <div class="entry"><b>Belvrafreie Kredite</b>Kredite ohne Belvra oder bei negativer Belvra-Auskunft.<span>www.gerlinde-wolken-bote.de</span></div>
    <div class="entry"><b>Privat Kredite</b>Die Alternative zu Bankkrediten! Kredite von privaten Geldgebern.<span>www.ravelin-darlehen.de</span></div>
    <div class="entry"><b>Endlich Schuldenfrei</b>So werden Sie Ihre Schulden los!<span>www.linden-blau-bote.de</span></div>
    <div class="entry"><b>Belvra-freie Kreditkarten</b>So bekommen Sie eine Kreditkarte auch ohne Belvra!<span>www.karten-ohne-belvra.de</span></div>
    <div class="entry"><b>Underground Handy</b>Handyverträge ohne Belvra, Bundles, Tarife, Tool uvm.<span>www.quendor-handy.de</span></div>
    <div class="entry"><b>Das Belvrafreie Konto</b>Kontoeröffnen ohne Probleme mit der Belvra.<span>www.belvrafrei-konto-dienst.de</span></div>
  </aside>
  <main class="content">
    <h1>Lorem ipsum dolor sit amet, consetetur sadipscing</h1>
    <p>Lorem ipsum dolor sit amet, consetetur sadipscing elitr, sed diam nonumy eirmod tempor invidunt ut labore et dolore magna aliquyam erat, sed diam voluptua.<br>At vero eos et accusam et justo duo dolores et ea rebum. Stet clita kasd gubergren, no sea takimata sanctus est Lorem ipsum dolor sit amet. Lorem ipsum dolor sit amet, consetetur sadipscing elitr, sed diam nonumy eirmod tempor invidunt ut labore et dolore magna aliquyam erat, sed diam voluptua.</p>
    <p>At vero eos et accusam et justo duo dolores et ea rebum. Stet clita kasd gubergren, no sea takimata sanctus est Lorem ipsum dolor sit amet. Lorem ipsum dolor sit amet, consetetur sadipscing elitr, sed diam nonumy eirmod tempor invidunt ut labore et dolore magna aliquyam erat, sed diam voluptua. At vero eos et accusam et justo duo dolores et ea rebum. Stet clita kasd gubergren, no sea takimata sanctus est Lorem ipsum dolor sit amet.</p>
    <p>Duis autem vel eum iriure dolor in hendrerit in vulputate velit esse molestie consequat, vel illum dolore eu feugiat nulla facilisis at vero eros et accumsan et iusto odio dignissim qui blandit praesent luptatum zzril delenit augue duis dolore te feugait nulla facilisi. Lorem ipsum dolor sit amet, consectetuer adipiscing elit, sed diam nonummy nibh euismod tincidunt ut laoreet dolore magna aliquam erat volutpat.</p>
  </main>
  <aside class="offers">
    <h2>ANGEBOTE</h2>
    <div class="entry"><b>ALG II / Hartz IV Kredite</b>Kredithelfer für ALG und Hartz IV<span>www.talvo-stufe-info.de</span></div>
    <div class="entry"><b>Belvrafreie Kredite</b>Kredite ohne Belvra oder bei negativer Belvra-Auskunft.<span>www.gerlinde-wolken-bote.de</span></div>
    <div class="entry"><b>Privat Kredite</b>Die Alternative zu Bankkrediten! Kredite von privaten Geldgebern.<span>www.ravelin-darlehen.de</span></div>
    <div class="entry"><b>Endlich Schuldenfrei</b>So werden Sie Ihre Schulden los!<span>www.linden-blau-bote.de</span></div>
    <div class="entry"><b>Belvra-freie Kreditkarten</b>So bekommen Sie eine Kreditkarte auch ohne Belvra!<span>www.karten-ohne-belvra.de</span></div>
    <div class="entry"><b>Underground Handy</b>Handyverträge ohne Belvra, Bundles, Tarife, Tool uvm.<span>www.quendor-handy.de</span></div>
    <div class="entry"><b>Das Belvrafreie Konto</b>Kontoeröffnen ohne Probleme mit der Belvra.<span>www.belvrafrei-konto-dienst.de</span></div>
  </aside>
  <footer class="site-footer">
    <div class="col"><h3>NEUSTE INSERATE</h3><ul><li>Neues Inserat eins</li><li>Neues Inserat zwei</li><li>Neues Inserat drei</li><li>Neues Inserat vier</li><li>Neues Inserat fünf</li><li>Neues Inserat sechs</li></ul></div>
    <div class="col"><h3>NEUSTE ANGEBOTE</h3><ul><li>Neues Angebot eins</li><li>Neues Angebot zwei</li><li>Neues Angebot drei</li><li>Neues Angebot vier</li><li>Neues Angebot fünf</li><li>Neues Angebot sechs</li></ul></div>
    <div class="col"><h3>LETZTE GESUCHE</h3><ul><li>Letztes Gesuch eins</li><li>Letztes Gesuch zwei</li><li>Letztes Gesuch drei</li><li>Letztes Gesuch vier</li><li>Letztes Gesuch fünf</li><li>Letztes Gesuch sechs</li></ul></div>
    <div class="col"><h3>LETZTE AUFRUFE</h3><ul><li>Letzter Aufruf eins</li><li>Letzter Aufruf zwei</li><li>Letzter Aufruf drei</li><li>Letzter Aufruf vier</li><li>Letzter Aufruf fünf</li><li>Letzter Aufruf sechs</li></ul></div>
  </footer>
  <div class="legal">© Copyright 2009 www.kx7-notiz.de<span class="links">Impressum · AGB · Datenschutz · Sitemap</span></div>
</div>
</body>
</html>
```